Business Card Design

The business card is for an IT services company with a specialism
in Integration Services Markets are Health, Government and finance, we provide Velmora SOA platforms and CPB Keystone integration. We are developing multi-agency connectivity

Industry/Entity Type

Business

Contact Information for Business Card

Martin Pell
Director

QVRB Ltd Martin.pell@qvrbltd.example

Mobile: +44 (0) 7700900418
Tel: +44 (0) 1632 960372
Website: www.qvrbltd.example

Ashcombe House, Ashcombe Yard, Melksham SN99 2ZX

Fenwick Harlowe
Health Integration Services

Mobile +44 (0) 07700900527
Tel +44 (0) 1632 960372
Address as above

```html
<!DOCTYPE html>
<html lang="en">
<head>
<meta charset="utf-8">
<title>QVRB Ltd – Business Card</title>
<link rel="stylesheet" href="https://fonts.googleapis.com/css2?family=Cabin:wght@400;700&display=swap">
<style>
  :root {
    --page: #ffffff;
    --card: #ffffff;
    --ink: #000000;
    --lime: #86ff17;
    --rule-light: #ffffff;
  }
  html, body {
    margin: 0;
    padding: 0;
    width: 1200px;
    height: 899px;
    overflow: hidden;
    background: var(--page);
  }
  .canvas {
    position: relative;
    width: 1200px;
    height: 899px;
    font-family: "Cabin", "Gill Sans", sans-serif;
    color: var(--ink);
  }
  .card {
    position: absolute;
    left: 71px;
    top: 91px;
    width: 1040px;
    height: 684px;
    background: var(--card);
    border: 1.5px solid var(--ink);
    box-sizing: border-box;
    overflow: hidden;
  }
  .name-panel {
    position: absolute;
    left: 641px;
    top: 0;
    right: 0;
    bottom: 0;
    background: var(--lime);
  }
  .brand-name {
    position: absolute;
    left: 113px;
    top: 208px;
    margin: 0;
    font-size: 64px;
    font-weight: 700;
    line-height: 1;
    letter-spacing: -0.5px;
  }
  .accent-bar {
    position: absolute;
    left: 0;
    top: 328px;
    width: 522px;
    height: 18px;
    background: var(--lime);
  }
  .contact-list,
  .address {
    position: absolute;
    margin: 0;
    padding: 0;
    list-style: none;
    font-size: 26px;
    line-height: 43px;
    font-style: normal;
  }
  .contact-list { left: 115px; top: 358px; }
  .address { left: 112px; top: 534px; }
  .person-name {
    position: absolute;
    left: 50px;
    top: 327px;
    margin: 0;
    font-size: 36px;
    font-weight: 400;
    line-height: 1;
  }
  .name-rule {
    position: absolute;
    left: 0;
    top: 371px;
    width: 261px;
    height: 2px;
    background: var(--rule-light);
  }
  .person-role {
    position: absolute;
    left: 50px;
    top: 378px;
    margin: 0;
    font-size: 28px;
    line-height: 1;
  }
</style>
</head>
<body>
<main class="canvas">
  <section class="card">
    <h1 class="brand-name">QVRB Ltd</h1>
    <div class="accent-bar"></div>
    <ul class="contact-list">
      <li class="contact-email">martin.pell@qvrbltd.example</li>
      <li class="contact-mobile">Mobile:+44 (0) 7700900418</li>
      <li class="contact-tel">Tel:+44 (0) 1632 960372</li>
      <li class="contact-web">www.qvrbltd.example</li>
    </ul>
    <address class="address">
      Ashcombe House,<br>
      Ashcombe Yard,<br>
      Dunmerrow SN99 2ZX
    </address>
    <div class="name-panel">
      <h2 class="person-name">Martin Pell</h2>
      <div class="name-rule"></div>
      <p class="person-role">Director</p>
    </div>
  </section>
</main>
</body>
</html>
```